Bramblecourt Homes Stationary
Fast Settlements
Professional
Dorian Pelletier
Managing Member
4817 Larkspur Ave Suite 210
Washington, DC
dgpelletier@bramblecourthomes.net
www.bramblecourthomes.net
Business License # 782645113058
Cash Buyer, Fast Closing.
Residential and Commercial
We are a Nation Wide Buyer.
will upload ai file shortly
vector logo file

```html
<!DOCTYPE html>
<html lang="en">
<head>
<meta charset="utf-8">
<title>Bramblecourt Homes Stationary</title>
<link href="https://fonts.googleapis.com/css2?family=Montserrat:wght@500;600;700&display=swap" rel="stylesheet">
<style>
  :root {
    --page-bg: #e9e7e3;
    --card-bg: #ffffff;
    --brand-green: #1d8a3c;
    --band-green: #1f9a44;
    --band-edge: #1a1a1a;
    --rule-grey: #8a8a8a;
    --ink-light: #ffffff;
  }
  * { margin: 0; padding: 0; box-sizing: border-box; }
  html, body { width: 1200px; height: 914px; overflow: hidden; }
  body {
    background: var(--page-bg);
    font-family: "Montserrat", Arial, sans-serif;
    position: relative;
  }
  .business-card {
    position: absolute;
    left: 100px; top: 171px;
    width: 1000px; height: 572px;
    background: var(--card-bg);
    box-shadow: 0 6px 24px rgba(0,0,0,0.12);
  }
  .brand {
    position: absolute;
    left: 0; right: 0; top: 110px;
    display: flex; flex-direction: column; align-items: center;
  }
  .brand-lockup { display: flex; align-items: center; gap: 16px; }
  .brand-square { width: 30px; height: 30px; background: var(--brand-green); }
  .brand-name {
    font-weight: 700; font-size: 50px; letter-spacing: 2px;
    color: var(--brand-green); text-transform: uppercase;
  }
  .brand-rule {
    margin-top: 14px; width: 420px; height: 1px; background: var(--rule-grey);
  }
  .name-band {
    position: absolute; left: 0; right: 0; top: 292px; height: 62px;
    background: var(--band-green);
    border-top: 3px solid var(--band-edge);
    border-bottom: 3px solid var(--band-edge);
    display: flex; align-items: center; justify-content: center;
    color: var(--ink-light); font-size: 22px; font-weight: 500;
    font-variant: small-caps; letter-spacing: 1.5px;
  }
  .name-band .divider { margin: 0 14px; opacity: 0.9; }
  .contact {
    position: absolute; left: 36px; right: 36px; top: 384px;
    display: flex; justify-content: space-between; gap: 36px;
    color: var(--brand-green); font-size: 15px; font-weight: 600;
    font-variant: small-caps; letter-spacing: 0.6px;
  }
  .contact-col { display: flex; flex-direction: column; gap: 14px; }
  .contact-row { display: flex; align-items: center; gap: 20px; }
  .contact-item { display: flex; align-items: center; gap: 8px; white-space: nowrap; }
  .icon { width: 18px; height: 18px; flex: none; }
  .bottom-rule {
    position: absolute; left: 0; right: 0; bottom: 40px; height: 4px;
    background: var(--band-green);
  }
</style>
</head>
<body>
  <div class="business-card">
    <div class="brand">
      <div class="brand-lockup">
        <span class="brand-square"></span>
        <span class="brand-name">Bramblecourt Homes</span>
      </div>
      <div class="brand-rule"></div>
    </div>

    <div class="name-band">
      <span>Dorian Pelletier</span><span class="divider">|</span><span>Managing Member</span>
    </div>

    <div class="contact">
      <div class="contact-col">
        <div class="contact-row">
          <span class="contact-item">
            <svg class="icon" viewBox="0 0 20 20"><circle cx="10" cy="10" r="10" fill="#1d8a3c"/><path d="M7 5.5l2 2-1 1.2c.6 1.3 1.6 2.3 2.9 2.9l1.2-1 2 2-1.2 1.5C9.8 14 6 10.2 5.5 7.1z" fill="#fff"/></svg>
            1-800-555-0142
          </span>
          <span class="contact-item">
            <svg class="icon" viewBox="0 0 20 20"><circle cx="10" cy="10" r="10" fill="#1d8a3c"/><path d="M7 5.5l2 2-1 1.2c.6 1.3 1.6 2.3 2.9 2.9l1.2-1 2 2-1.2 1.5C9.8 14 6 10.2 5.5 7.1z" fill="#fff"/></svg>
            202-555-0187
          </span>
          <span class="contact-item">
            <svg class="icon" viewBox="0 0 20 20"><circle cx="10" cy="10" r="10" fill="#1d8a3c"/><path d="M7 5.5l2 2-1 1.2c.6 1.3 1.6 2.3 2.9 2.9l1.2-1 2 2-1.2 1.5C9.8 14 6 10.2 5.5 7.1z" fill="#fff"/></svg>
            410-555-0163
          </span>
        </div>
        <div class="contact-row">
          <span class="contact-item">
            <svg class="icon" viewBox="0 0 20 20"><circle cx="10" cy="10" r="10" fill="#1d8a3c"/><path d="M10 4.5a3.5 3.5 0 0 1 3.5 3.5c0 2.6-3.5 7-3.5 7s-3.5-4.4-3.5-7A3.5 3.5 0 0 1 10 4.5z" fill="#fff"/><circle cx="10" cy="8" r="1.3" fill="#1d8a3c"/></svg>
            4817 Larkspur Ave Suite 210 Washington, DC 20006
          </span>
        </div>
      </div>
      <div class="contact-col">
        <span class="contact-item">
          <svg class="icon" viewBox="0 0 20 20"><circle cx="10" cy="10" r="10" fill="#1d8a3c"/><rect x="5" y="6.5" width="10" height="7" fill="#fff"/><path d="M5 6.5l5 4 5-4" fill="none" stroke="#1d8a3c" stroke-width="1"/></svg>
          dgpelletier@bramblecourthomes.net
        </span>
        <span class="contact-item">
          <svg class="icon" viewBox="0 0 20 20"><circle cx="10" cy="10" r="10" fill="#1d8a3c"/><circle cx="10" cy="10" r="5" fill="none" stroke="#fff" stroke-width="1.2"/><path d="M5 10h10M10 5c-2 3-2 7 0 10M10 5c2 3 2 7 0 10" fill="none" stroke="#fff" stroke-width="1"/></svg>
          www.bramblecourthomes.net
        </span>
      </div>
    </div>

    <div class="bottom-rule"></div>
  </div>
</body>
</html>
```